Personal Training Studio Checkin App (or URL based)

I would like a simple web based app built for our  business. We have a training studio with a simple business model. All our clients buy sessions in packages either 4, 8, or 12 at a time. We want something that a trainer can pull up and Check in a client. This will record the date and time the client was checked in, by what trainer, and what type of session. This system will keep track of the following:
Whenever a Client Checks in so it will ‘tick off’ a session on their package (ie- they have gone from 11 sessions left to 10 sessions left)
Track what sessions a particular trainer does so we can pay them at the end of the week and look at who they trained, what type of session and how many
Look at client activity: Every time they check in, Recharge their package, any activity related to the client, even if it was admin – like deleting a session that was mistakenly recorded.
This will keep a database of clients added and all their activity
The pdf I have included lays out how I think it would work and the features I want
I would like this to run off an vornix that we have at our front check in counter. It can be an app or a URL that use.
***THIS PROJECT IS NOT SO MUCH ABOUT DESIGN BUT ABOUT FUNCTIONALITY OF THE APPLICATION. IT MUST HAVE THE FEATURES I HAVE ASKED FOR THAT WORK TOGETHER. I AM WILLING TO PAY A LITTLE MORE AS A BONUS IF YOU CAN ACCOMPLISH THIS. ALSO IF I FIN THE RIGHT PERSON THAT CAN DO THIS I WILL MAKE IT A GUARNTEED PROJECT.

- Functionality and Track and record all the info we need

```html
<!DOCTYPE html>
<html lang="en">
<head>
<meta charset="utf-8">
<title>Corevale — Admin Panel Login</title>
<link rel="stylesheet" href="https://fonts.googleapis.com/css2?family=Noto+Sans:wght@400;500;600&display=swap">
<style>
  :root {
    --bg-dark: #1c1c1e;
    --bg-mid: #4a4a4c;
    --bg-light: #8e8e90;
    --card: #ffffff;
    --ink: #212529;
    --brand: #5b5b5d;
    --accent: #f04e1a;
    --border: #dee2e6;
    --primary: #0d6efd;
    --link: #0d6efd;
  }
  * { box-sizing: border-box; margin: 0; padding: 0; }
  html, body {
    width: 1200px; height: 834px; overflow: hidden;
    font-family: "Noto Sans", "Segoe UI", sans-serif;
    color: var(--ink);
  }
  .login-page { position: relative; width: 1200px; height: 834px; }
  .hero-photo {
    position: absolute; inset: 0;
    background:
      radial-gradient(ellipse at 85% 20%, var(--bg-light) 0%, transparent 45%),
      radial-gradient(ellipse at 70% 90%, #6a6a6c 0%, transparent 40%),
      linear-gradient(120deg, var(--bg-dark) 0%, var(--bg-mid) 45%, #6c6c6e 70%, #3a3a3c 100%);
  }
  .login-card {
    position: absolute; left: 397px; top: 180px;
    width: 406px; height: 474px;
    background: var(--card);
    border-radius: 5px;
    padding: 0 50px;
  }
  .brand {
    margin-top: 54px;
    display: flex; align-items: center; justify-content: center; gap: 8px;
    height: 44px;
  }
  .brand-mark { width: 16px; height: 16px; background: var(--accent); }
  .brand-name {
    font-size: 30px; font-weight: 600; color: var(--brand); letter-spacing: -0.5px;
  }
  .login-title {
    margin-top: 22px;
    text-align: center; font-size: 20px; font-weight: 500;
  }
  .login-form { margin-top: 24px; }
  .field-label { display: block; font-size: 16px; line-height: 20px; }
  .field-input {
    display: block; width: 100%; height: 38px; margin-top: 10px;
    border: 1px solid var(--border); border-radius: 5px;
    font: inherit; padding: 0 12px;
  }
  .field + .field { margin-top: 14px; }
  .login-button {
    display: block; width: 100%; height: 38px; margin-top: 18px;
    background: var(--primary); color: #fff; border: 0; border-radius: 5px;
    font: inherit; font-size: 16px;
  }
  .forgot-link {
    display: block; margin-top: 20px; text-align: center;
    color: var(--link); font-size: 16px; text-decoration: underline;
  }
</style>
</head>
<body>
<main class="login-page">
  <div class="hero-photo" role="img" aria-label="Trainer and client lifting barbells in a gym"></div>
  <section class="login-card">
    <div class="brand">
      <span class="brand-mark"></span>
      <span class="brand-name">Corevale</span>
    </div>
    <h1 class="login-title">Admin Panel Login</h1>
    <form class="login-form">
      <div class="field">
        <label class="field-label" for="username">Username</label>
        <input class="field-input" id="username" type="text">
      </div>
      <div class="field">
        <label class="field-label" for="password">Password</label>
        <input class="field-input" id="password" type="password">
      </div>
      <button class="login-button" type="button">Login</button>
      <a class="forgot-link" href="#">Forgot Password?</a>
    </form>
  </section>
</main>
</body>
</html>
```